Payment company requires web design

We need a web design for a new company based in Singapore.

The company focuses on providing 2 key products: 1) an alternative payment option (i.e. like plorix or quentabank options) on the traditional checkout process 2) a replacement/outsource of a merchants payment page. Key in the UX flow is a end customer dashboard that manages all payments.

We look to provide a simple, fluid and easy to use payment process. The dashboard is minimalistic that allows easy navigation, review of transactions and all available options through gamification.

The final design should communicate ease of use, flexibility and transparency.

Target Market(s)

The value is for the merchant - retail/travel/insurance companies. However its the merchant's end customers that are the target and who the UX is built for.

Industry/Entity Type

It Company

Logo Text

dravin

Number of Pages Required

5+ page

Colors
ec1f27

Requirements
Must have
• 7 pages mimicking UX flow
• payment page * 2 - 1) alternative payment type 2) outsource of merchants payment page to our business
• our landing page
• end customer verification page
• end customer registration
• customer dashboard
• UX flow in attached file
Nice to have
• open to ideas
• have asked for the logo to be added
• logo to have the colour red (chinese for prosperity)
• the company is all about flexibility, transparency in personal finance management with the option of instalment payments

```html
<!DOCTYPE html>
<html lang="en">
<head>
<meta charset="utf-8">
<title>Dravin — Payment Processing</title>
<link rel="stylesheet" href="https://fonts.googleapis.com/css2?family=Montserrat:wght@500;600&family=Raleway:wght@300;400;500&display=swap">
<style>
  :root {
    --brand: #b23535;
    --brand-dark: #a02d2d;
    --ink: #555555;
    --ink-soft: #777777;
    --muted: #c8c8c8;
    --line: #ececec;
    --footer-bg: #f9f9f9;
    --white: #ffffff;
  }
  * { box-sizing: border-box; margin: 0; padding: 0; }
  html, body { width: 842px; height: 1200px; overflow: hidden; background: var(--white); }
  body { position: relative; font-family: "Raleway", Arial, sans-serif; color: var(--ink); }
  .abs { position: absolute; }

  /* Hero */
  .hero { position: absolute; left: 0; top: 0; width: 842px; height: 464px; overflow: hidden; }
  .hero-photo {
    position: absolute; inset: 0;
    background:
      radial-gradient(ellipse at 40% 35%, rgba(150,110,90,.55), transparent 55%),
      radial-gradient(ellipse at 75% 80%, rgba(120,80,50,.7), transparent 50%),
      linear-gradient(135deg, #3b3430 0%, #6b5a50 35%, #4a4f5e 55%, #8a6a4c 80%, #5a4030 100%);
  }
  .hero-shade { position: absolute; inset: 0; background: rgba(20,15,12,.25); }
  .logo { font-family: "Montserrat", Arial, sans-serif; font-weight: 500; font-size: 21px; letter-spacing: 1px; }
  .hero .logo { left: 134px; top: 30px; color: var(--white); }
  .search {
    left: 311px; top: 30px; width: 185px; height: 24px; border: 1px solid var(--white);
    border-radius: 12px; color: var(--white); font-size: 7px; padding: 0 10px;
    display: flex; align-items: center; justify-content: space-between;
  }
  .nav { top: 38px; color: var(--white); font-size: 7.5px; font-weight: 500; }
  .hero-title { left: 0; width: 842px; top: 242px; text-align: center; color: var(--white); font-size: 17.5px; font-weight: 400; }
  .btn {
    display: flex; align-items: center; justify-content: center; border-radius: 16px;
    font-size: 8.5px; font-weight: 500; letter-spacing: .2px;
  }
  .btn-primary { background: var(--brand); color: var(--white); }
  .btn-light { background: var(--white); color: var(--brand); }
  .hero .btn { left: 342px; top: 283px; width: 156px; height: 31px; border-radius: 16px; }
  .dot { top: 425px; width: 6px; height: 6px; border-radius: 50%; background: var(--white); }
  .dot.active { background: var(--brand); }

  /* About */
  .section-title { left: 0; width: 842px; top: 522px; text-align: center; color: var(--brand); font-size: 18px; font-weight: 400; }
  .intro { left: 140px; width: 562px; top: 563px; text-align: center; font-size: 8.4px; line-height: 16px; color: var(--ink-soft); }
  .feature { width: 160px; text-align: center; font-size: 8.6px; font-weight: 500; color: var(--ink); top: 628px; }
  .feature svg { display: block; margin: 0 auto 16px; }
  .divider { left: 141px; width: 559px; height: 1px; background: var(--line); }

  /* Cards */
  .card { top: 778px; width: 271px; height: 188px; border-radius: 16px; padding: 34px 19px 0; }
  .card-info { left: 142px; background: var(--brand); color: var(--white); }
  .card-service { left: 429px; background: var(--white); border: 1px solid var(--line); }
  .card-head { display: flex; align-items: center; gap: 14px; font-size: 18px; font-weight: 300; height: 20px; }
  .card-service .card-head { color: var(--ink-soft); gap: 10px; }
  .card-text { margin-top: 15px; font-size: 12px; line-height: 19px; font-weight: 400; }
  .card-service .card-text { color: var(--muted); font-weight: 300; }
  .card .btn { position: absolute; left: 17px; top: 142px; width: 104px; height: 30px; }

  /* Footer */
  .footer { left: 0; top: 1029px; width: 842px; height: 137px; background: var(--footer-bg); }
  .footer .logo { left: 134px; top: 48px; color: var(--brand); font-size: 21px; font-weight: 600; }
  .footer-links { top: 48px; list-style: none; font-size: 7px; line-height: 16px; color: var(--ink); }
  .social { left: 610px; top: 51px; display: flex; gap: 6px; font-size: 6.5px; font-weight: 500; color: var(--brand); }
  .footer-bar { left: 0; top: 1166px; width: 842px; height: 34px; border-top: 1px solid var(--line); text-align: center; font-size: 7px; line-height: 32px; color: var(--ink); }
</style>
</head>
<body>

<header class="hero">
  <div class="hero-photo" role="img" aria-label="Photo of a customer paying with a card terminal at a café table"></div>
  <div class="hero-shade"></div>
  <div class="abs logo">DRAVIN</div>
  <div class="abs search"><span>SEARCH</span>
    <svg width="8" height="8" viewBox="0 0 10 10"><circle cx="4.2" cy="4.2" r="3" fill="none" stroke="#fff" stroke-width="1.6"/><line x1="6.4" y1="6.4" x2="9" y2="9" stroke="#fff" stroke-width="1.8"/></svg>
  </div>
  <nav>
    <span class="abs nav" style="left:533px">ABOUT</span>
    <span class="abs nav" style="left:584px">FAQ'S</span>
    <span class="abs nav" style="left:631px">CONTACT US</span>
  </nav>
  <h1 class="abs hero-title">WE ARE PAYMENT PROCESSING COMPANY FROM SINGAPORE</h1>
  <div class="abs btn btn-primary">GET STARTED NOW</div>
  <span class="abs dot active" style="left:398px"></span>
  <span class="abs dot" style="left:411px"></span>
  <span class="abs dot" style="left:424px"></span>
  <span class="abs dot" style="left:437px"></span>
</header>

<section>
  <h2 class="abs section-title">ABOUT DRAVIN</h2>
  <p class="abs intro">Sed ut perspiciatis unde omnis iste natus error sit voluptatem accusantium doloremque laudantium, totam rem aperiam, eaque ipsa quae ab illo inventore veritatis et quasi architecto beatae vitae dicta sunt explicabo. Nemo enim ipsam voluptatem</p>

  <div class="abs feature" style="left:148px">
    <svg width="28" height="24" viewBox="0 0 28 24" fill="none" stroke="#b23535" stroke-width="3">
      <path d="M1 6h6c5 0 8 12 13 12h4"/><path d="M1 18h6c5 0 8-12 13-12h4"/>
      <path d="M21 2l5 4-5 4M21 14l5 4-5 4" stroke-width="2.6"/>
    </svg>FLEXIBILITY</div>
  <div class="abs feature" style="left:340px">
    <svg width="28" height="26" viewBox="0 0 28 26"><path d="M27 1L2 12l7 3 2 10 4-7 7 3z" fill="#b23535"/><path d="M9 15L27 1" stroke="#fff" stroke-width="1.2"/></svg>TRANSPERENCY</div>
  <div class="abs feature" style="left:531px">
    <svg width="26" height="24" viewBox="0 0 26 24"><rect x="9" y="1" width="8" height="5" rx="1" fill="none" stroke="#b23535" stroke-width="2"/><rect x="0" y="5" width="26" height="18" rx="2" fill="#b23535"/><rect x="0" y="12" width="26" height="1.5" fill="#fff"/><rect x="10" y="10" width="6" height="5" fill="#fff"/></svg>INSTALMENT PAYMENT</div>

  <div class="abs divider" style="top:742px"></div>

  <article class="abs card card-info">
    <div class="card-head">
      <svg width="16" height="16" viewBox="0 0 16 16"><circle cx="8" cy="8" r="8" fill="#fff"/><rect x="7" y="7" width="2.4" height="5.5" fill="#b23535"/><circle cx="8.2" cy="4.6" r="1.4" fill="#b23535"/></svg>
      INFORMATION</div>
    <p class="card-text">Sed ut perspiciatis unde omnis iste natus error sit voluptatem accusantium doloremque.</p>
    <div class="btn btn-light">READ MORE</div>
  </article>

  <article class="abs card card-service">
    <div class="card-head">
      <svg width="16" height="16" viewBox="0 0 16 16"><circle cx="8" cy="4.5" r="4" fill="#b23535"/><path d="M0 16c0-5 3-7 8-7s8 2 8 7z" fill="#b23535"/></svg>
      CUSTOMER SERVICE</div>
    <p class="card-text">Sed ut perspiciatis unde omnis iste natus error sit voluptatem accusantium doloremque.</p>
    <div class="btn btn-primary">READ MORE</div>
  </article>

  <div class="abs divider" style="top:1006px"></div>
</section>

<footer class="abs footer">
  <div class="abs logo">DRAVIN</div>
  <ul class="abs footer-links" style="left:277px"><li>ABOUT</li><li>FAQ'S</li><li>CONTACT US</li></ul>
  <ul class="abs footer-links" style="left:373px"><li>LEADERSHIP TEAM</li><li>JOBS</li></ul>
  <ul class="abs footer-links" style="left:490px"><li>TERMS OF USE</li><li>PRIVACY POLICY</li></ul>
  <div class="abs social"><span>LINKR</span><span>POSTA</span><span>CHIRP</span><span>VIDD</span></div>
</footer>
<div class="abs footer-bar">© 2016 COMPANY NAME &nbsp;|&nbsp; ALL RIGHTS RESERVED</div>

</body>
</html>
```